Fundraiser Flyer and Email Template

We are looking for a flexible coordinated flyer and email template. The feel of both should be more formal or professional. We are not looking for an overly "political" design that features American flags or other "political" symbols.

We are a political fundraising firm that works with elected officials to set up fundraisers for their campaigns. We send the invites to these events via US Mail and email, so we are looking for a standardized template that will work as both an 8.5 x 11 inch printed flyer, as well as an email template.

The information in the email will be text, but images can be used for formatting.

Some clients have a campaign logo, others do not. The format should be flexible enough to either include the logo, or leave it out. Size also varies.

Any colors in the template should be editable so we can match logos as we get them.

We're open to any format that allows us to edit the format as needed. This would include Photoshop, Microsoft Word, etc.

The text of the invite should include space for:

---------------------------------------
NAME
DISTRICT NUMBER AND OFFICE

DATE OF EVENT
TIME OF EVENT

LOCATION
LOCATION ADDRESS
LOCATION CITY, STATE, ZIP

SUGGESTED CONTRIBUTION LEVELS (Typically 3 levels are provided such as Gold: $1,000, Silver: $500, Bronze: $250)

ADDRESS TO SEND CHECKS TO

RSVP CONTACT INFORMATION

The invite will also need fine-print at the bottom that reads:
"Pennsylvania law allows personal, partnership, and PAC contributions. By law we cannot accept corporate contributions
Paid for by [NAME]"

It Professional

Serif
Sans Serif

• Must have spaces for:
• NAME
• DISTRICT NUMBER AND OFFICE
• DATE OF EVENT
• TIME OF EVENT
• LOCATION
• LOCATION ADDRESS
• LOCATION CITY, STATE, ZIP
• SUGGESTED CONTRIBUTION LEVELS (Typically 3 levels are provided such as Gold: $1,000, Silver: $500, Bronze: $250)
• ADDRESS TO SEND CHECKS TO
• RSVP CONTACT INFORMATION
• The invite will also need fine-print at the bottom that reads:
• "Pennsylvania law allows personal, partnership, and PAC contributions. By law we cannot accept corporate contributions
• Paid for by [NAME]"
• It should not be overly "political".

```html
<!DOCTYPE html>
<html lang="en">
<head>
<meta charset="utf-8">
<title>Fundraising Reception Invitation</title>
<link href="https://fonts.googleapis.com/css2?family=Cinzel:wght@400;600&family=Archivo+Black&family=Roboto+Condensed:wght@400;700&display=swap" rel="stylesheet">
<style>
  :root{
    --backdrop:#e9e6e0;
    --white:#ffffff;
    --purple-deep:#4a2a92;
    --purple:#7b5fb4;
    --purple-mid:#8f82c8;
    --lavender:#cdc7e8;
    --navy-purple:#4a3f9e;
    --gold:#f6cf3a;
    --gold-light:#f7e07e;
    --silver:#e4e4ea;
    --bronze:#e8b48a;
    --photo-grey:#8b8b8b;
  }
  *{box-sizing:border-box;margin:0;padding:0}
  html,body{width:1200px;height:898px;overflow:hidden;background:var(--backdrop)}
  .flyer{
    position:absolute;left:267px;top:19px;width:666px;height:860px;overflow:hidden;
    background:linear-gradient(180deg,var(--white) 17%,var(--lavender) 42%,var(--purple-mid) 65%,var(--navy-purple) 88%);
    box-shadow:0 6px 18px rgba(0,0,0,.18);
    font-family:"Roboto Condensed",sans-serif;
    text-align:center;color:var(--purple-deep);
  }
  .header-band{position:absolute;left:0;top:0;width:666px;height:170px}
  .header-title{
    position:absolute;left:0;right:0;top:38px;
    font-family:"Cinzel",serif;font-size:25px;line-height:1.4;color:var(--white);letter-spacing:1px;
  }
  .header-title .star{color:var(--gold);font-size:18px;margin:0 8px}
  .brand{
    position:absolute;left:0;right:0;top:182px;
    display:flex;justify-content:center;align-items:center;gap:12px;
    font-family:"Archivo Black",sans-serif;font-size:40px;color:var(--purple-deep);
  }
  .brand-square{width:30px;height:30px;background:var(--gold)}
  .candidate-name{position:absolute;left:0;right:0;top:248px;font-family:"Archivo Black",sans-serif;font-size:36px;color:var(--purple-deep)}
  .candidate-office{position:absolute;left:0;right:0;top:296px;font-family:"Archivo Black",sans-serif;font-size:25px;color:var(--purple-deep)}
  .candidate-office sup{font-size:14px}
  .portrait{
    position:absolute;left:258px;top:345px;width:150px;height:150px;
    background:linear-gradient(180deg,#f4f4f4,var(--photo-grey));
    border:6px solid var(--white);box-shadow:8px 8px 0 var(--purple);
  }
  .date-ribbon{position:absolute;left:23px;top:470px;width:620px;height:70px}
  .date-text{
    position:absolute;left:0;right:0;top:485px;font-size:30px;font-weight:700;color:var(--purple-deep);
  }
  .venue{position:absolute;left:0;right:0;top:552px;font-size:26px;font-weight:700;line-height:1.25;color:var(--purple-deep)}
  .contributions{position:absolute;left:0;right:0;top:622px;color:var(--white)}
  .contributions-title{font-size:19px;font-weight:400;text-decoration:underline;letter-spacing:.5px}
  .levels{font-size:17px;margin-top:5px;display:flex;justify-content:center;gap:16px;align-items:center}
  .dot{display:inline-block;width:9px;height:9px;border-radius:50%;margin-right:5px;vertical-align:middle}
  .dot.gold{background:var(--gold-light)}
  .dot.silver{background:var(--silver)}
  .dot.bronze{background:var(--bronze)}
  .checks{font-size:18px;font-weight:700;margin-top:5px;line-height:1.25}
  .footer-wave{position:absolute;left:0;top:730px;width:666px;height:130px}
  .footer-stars{position:absolute;left:0;right:0;top:756px;color:var(--gold);font-size:22px;line-height:1;letter-spacing:6px}
  .rsvp{
    position:absolute;left:0;right:0;top:786px;font-size:15px;font-weight:700;color:var(--purple-deep);
    display:flex;justify-content:center;align-items:center;gap:10px;
  }
  .rsvp svg{width:14px;height:14px;fill:var(--purple)}
  .fine-print{position:absolute;left:0;right:0;top:808px;font-size:11.5px;line-height:1.3;color:var(--purple)}
</style>
</head>
<body>
  <main class="flyer">
    <svg class="header-band" viewBox="0 0 666 170" aria-hidden="true">
      <defs>
        <linearGradient id="bandFill" x1="0" y1="0" x2="0" y2="1">
          <stop offset="0" stop-color="#8a6cc0"/>
          <stop offset="1" stop-color="#5e3a9e"/>
        </linearGradient>
      </defs>
      <path d="M0 0H666V118Q360 150 0 150Z" fill="url(#bandFill)"/>
      <path d="M0 150Q360 150 666 118" fill="none" stroke="#f6cf3a" stroke-width="3"/>
    </svg>
    <h2 class="header-title"><span class="star">★</span>Please Join Us for a<span class="star">★</span><br>Special Fundraising Reception</h2>

    <div class="brand"><span class="brand-square"></span>Whitmore</div>
    <h1 class="candidate-name">Daniel Whitmore</h1>
    <p class="candidate-office">State Senator, 46<sup>th</sup> Senate District</p>

    <div class="portrait" role="img" aria-label="Candidate portrait photo"></div>

    <svg class="date-ribbon" viewBox="0 0 620 70" aria-hidden="true">
      <defs>
        <linearGradient id="ribbonFill" x1="0" y1="0" x2="0" y2="1">
          <stop offset="0" stop-color="#f8e386"/>
          <stop offset="1" stop-color="#f4cc3a"/>
        </linearGradient>
      </defs>
      <path d="M0 8H620L600 35L620 62H0L20 35Z" fill="url(#ribbonFill)"/>
    </svg>
    <p class="date-text">Tuesday, June 17th &nbsp;|&nbsp; 5:00pm - 7:00pm</p>

    <p class="venue">Harbor Light Gallery, 120 Cedar Lane,<br>Lakeview, FL 33061</p>

    <section class="contributions">
      <h3 class="contributions-title">CONTRIBUTION LEVELS</h3>
      <p class="levels">
        <span><span class="dot gold"></span>Gold: $1,000</span>
        <span><span class="dot silver"></span>Silver: $500</span>
        <span><span class="dot bronze"></span>Bronze: $250</span>
      </p>
      <p class="checks">Make checks payable to : XXXXXXXXXXX<br>P.O. Box 5710, Brookside, FL 33445-5710</p>
    </section>

    <svg class="footer-wave" viewBox="0 0 666 130" aria-hidden="true">
      <path d="M0 60Q300 5 666 0V130H0Z" fill="#ffffff"/>
      <path d="M0 60Q300 5 666 0" fill="none" stroke="#4a2a92" stroke-width="3"/>
    </svg>
    <div class="footer-stars">★★★</div>
    <p class="rsvp">
      <span>RSVP CONTACT</span>
      <svg viewBox="0 0 24 24" aria-hidden="true"><path d="M6.6 10.8a15.1 15.1 0 0 0 6.6 6.6l2.2-2.2a1 1 0 0 1 1-.25 11.4 11.4 0 0 0 3.6.57 1 1 0 0 1 1 1V20a1 1 0 0 1-1 1A17 17 0 0 1 3 4a1 1 0 0 1 1-1h3.5a1 1 0 0 1 1 1c0 1.25.2 2.45.57 3.57a1 1 0 0 1-.25 1z"/></svg>
      <span>555-010-2468</span>
      <svg viewBox="0 0 24 24" aria-hidden="true"><path d="M2 5h20v14H2z M2 5l10 8 10-8" fill="none" stroke="#7b5fb4" stroke-width="2"/></svg>
      <span>rsvp@whitmorefund.org</span>
    </p>
    <p class="fine-print">Pennsylvania law allows personal, partnership, and PAC contributions.<br>By law we cannot accept corporate contributions<br>Paid for by [NAME]</p>
  </main>
</body>
</html>
```